Northgate Baptist Church Banner Design

Designing 6 banners (3 + 3 that will hang on opposite sides of our auditorium) that are 10 feet long by 4 feet wide.

Use our branding guide - specifically item 4 (vertical logo) and item 5 (icon logo).

Design elements found in our ASCEND booklet, we would like to see designs that utilize the white, green and blue colour palettes but NOT the grey. Other colours may be incorporated (e.g. coral).

We are looking for 3 banner designs that would match on either side of the auditorium, the first banner incorporating the word "TRUTH", the second incorporating the word "LOVE", and the third incorporating the word "MISSION".

We interested in incorporating graphics such as trees or outdoor themes.

Font styles to use
Other font styles liked:
• Montserrat

Colors
34a7d7
00a990
f47c35

Requirements
Must have
• Banner Type #1 include the word "TRUTH"
Banner Type #2 include the word "LOVE"
Banner Type #3 include the word "MISSION"

Colour scheme must include CMYK 54 / 5 / 16 / 0 (which is available in the branding guide.) We have selected the three colours, included below in the brief.

From the branding guide - utilize #5 (icon) for the banner.

UPDATE: After reviewing the initial submissions, we are asking for designs that ONLY incorporate #5 - the ICON logo for the banners.
Nice to have
• It would be nice to have some creativity with the colour ... though a more minimalistic style is preferred.

Graphic adaptations such as trees in the background would be of interest.
Should not have
• Colour scheme should not be gray scale.

The banners should NOT be too busy.

Scripture verses (written out) are not necessary.

```html
<!DOCTYPE html>
<html lang="en">
<head>
<meta charset="utf-8">
<title>Northgate Baptist Church – Banner Set</title>
<link href="https://fonts.googleapis.com/css2?family=Montserrat:wght@700&display=swap" rel="stylesheet">
<style>
  :root {
    --sky: #6cc0d0;
    --paper: #ffffff;
    --deep: #2f8596;
    --canvas: #ffffff;
  }
  html, body {
    margin: 0;
    padding: 0;
    width: 1200px;
    height: 933px;
    overflow: hidden;
    background: var(--canvas);
  }
  .banner-set {
    position: relative;
    width: 1200px;
    height: 933px;
  }
  .banner {
    position: absolute;
    top: 135px;
    width: 263px;
    height: 658px;
    background: var(--sky);
    overflow: hidden;
    box-shadow: 2px 3px 4px rgba(0,0,0,0.35);
    font-family: "Montserrat", sans-serif;
  }
  .banner--truth { left: 135px; }
  .banner--love { left: 475px; }
  .banner--mission { left: 815px; }

  .church-mark {
    position: absolute;
    left: 56px;
    top: 33px;
    width: 150px;
    height: 150px;
    border: 4px solid var(--paper);
    border-radius: 50%;
    box-sizing: border-box;
  }
  .church-name {
    position: absolute;
    left: 0;
    top: 202px;
    width: 100%;
    margin: 0;
    text-align: center;
    color: var(--paper);
    font-weight: 700;
    line-height: 1;
  }
  .church-name__main {
    display: block;
    font-size: 30px;
    letter-spacing: 0.5px;
  }
  .church-name__sub {
    display: block;
    margin-top: 9px;
    font-size: 17px;
    letter-spacing: 2.4px;
  }
  .church-name__place {
    display: block;
    margin-top: 7px;
    font-size: 8px;
    letter-spacing: 16px;
    padding-left: 16px;
  }

  .value-band {
    position: absolute;
    left: 0;
    top: 318px;
    width: 263px;
    height: 142px;
  }
  .value-word {
    position: absolute;
    left: 0;
    top: 366px;
    width: 100%;
    margin: 0;
    text-align: center;
    font-size: 50px;
    font-weight: 700;
    color: var(--sky);
    line-height: 1;
    letter-spacing: 0.5px;
  }

  .treeline {
    position: absolute;
    left: 0;
    bottom: 0;
    width: 263px;
    height: 150px;
    background: linear-gradient(to bottom, var(--sky) 0%, #5fb3c4 25%, var(--deep) 100%);
  }
</style>
</head>
<body>
<main class="banner-set">

  <section class="banner banner--truth">
    <div class="church-mark"></div>
    <p class="church-name">
      <span class="church-name__main">NORTHGATE</span>
      <span class="church-name__sub">BAPTIST CHURCH</span>
      <span class="church-name__place">EASTBROOK</span>
    </p>
    <svg class="value-band" viewBox="0 0 263 142" aria-hidden="true">
      <polygon fill="#ffffff" points="0,10 8,8 14,9 22,5 30,8 38,6 46,7 54,3 62,6 70,4 78,7 86,5 94,6 102,3 110,6 118,4 126,6 134,2 142,5 150,3 158,6 166,4 174,5 182,2 190,5 198,4 206,6 214,3 222,6 230,5 238,7 246,4 254,6 263,5 263,132 256,134 248,131 240,135 232,132 224,136 216,133 208,135 200,131 192,135 184,133 176,136 168,132 160,135 152,133 144,137 136,132 128,135 120,133 112,136 104,131 96,135 88,133 80,136 72,132 64,135 56,133 48,136 40,132 32,135 24,133 16,136 8,132 0,134"/>
    </svg>
    <h2 class="value-word">TRUTH</h2>
    <div class="treeline" role="img" aria-label="Silhouette of a row of trees on a hillside"></div>
  </section>

  <section class="banner banner--love">
    <div class="church-mark"></div>
    <p class="church-name">
      <span class="church-name__main">NORTHGATE</span>
      <span class="church-name__sub">BAPTIST CHURCH</span>
      <span class="church-name__place">EASTBROOK</span>
    </p>
    <svg class="value-band" viewBox="0 0 263 142" aria-hidden="true">
      <polygon fill="#ffffff" points="0,10 8,8 14,9 22,5 30,8 38,6 46,7 54,3 62,6 70,4 78,7 86,5 94,6 102,3 110,6 118,4 126,6 134,2 142,5 150,3 158,6 166,4 174,5 182,2 190,5 198,4 206,6 214,3 222,6 230,5 238,7 246,4 254,6 263,5 263,132 256,134 248,131 240,135 232,132 224,136 216,133 208,135 200,131 192,135 184,133 176,136 168,132 160,135 152,133 144,137 136,132 128,135 120,133 112,136 104,131 96,135 88,133 80,136 72,132 64,135 56,133 48,136 40,132 32,135 24,133 16,136 8,132 0,134"/>
    </svg>
    <h2 class="value-word">LOVE</h2>
    <div class="treeline" role="img" aria-label="Silhouette of a row of trees on a hillside"></div>
  </section>

  <section class="banner banner--mission">
    <div class="church-mark"></div>
    <p class="church-name">
      <span class="church-name__main">NORTHGATE</span>
      <span class="church-name__sub">BAPTIST CHURCH</span>
      <span class="church-name__place">EASTBROOK</span>
    </p>
    <svg class="value-band" viewBox="0 0 263 142" aria-hidden="true">
      <polygon fill="#ffffff" points="0,10 8,8 14,9 22,5 30,8 38,6 46,7 54,3 62,6 70,4 78,7 86,5 94,6 102,3 110,6 118,4 126,6 134,2 142,5 150,3 158,6 166,4 174,5 182,2 190,5 198,4 206,6 214,3 222,6 230,5 238,7 246,4 254,6 263,5 263,132 256,134 248,131 240,135 232,132 224,136 216,133 208,135 200,131 192,135 184,133 176,136 168,132 160,135 152,133 144,137 136,132 128,135 120,133 112,136 104,131 96,135 88,133 80,136 72,132 64,135 56,133 48,136 40,132 32,135 24,133 16,136 8,132 0,134"/>
    </svg>
    <h2 class="value-word">MISSION</h2>
    <div class="treeline" role="img" aria-label="Silhouette of a row of trees on a hillside"></div>
  </section>

</main>
</body>
</html>
```